Harrowgate Building and Property Services needs a business card design

We need a business card design for our building and property services business. We already have a logo we just need a creative design and layout on a business card. Emphasis on clean, modern, professional.
Our client targets are mainly body corporates, building managers, construction managers.
We are a building services company that lean more to structural repair of buildings, through concrete rectification and carbon fibre strengthening.
We also refurbish facades, rendering, painting etc
We target higher end body corporates in prestigious locations, hence why we'd like our cards to reflect professionalism, strength, efficiency

Target Market(s)

body corporates, building managers, construction managers

Industry/Entity Type

Construction

Contact Information for Business Card

Harrowgate is the main word, with 'Building and Property Services' underneath.
Level 17, 88 Marsh Lane
ELMSWORTH
Melbourne
Vic 3942
T: 9218 5371
Duncan Hensley - Director
dunharrowgate@mailbox-example.net

Requirements
Must have
• Stand out on the back of the card- strong/ bold, company logo
• All of the contact details written above
Should not have
• I'd like the card to stand out, especially on the back. Id like the company logo to be prominent, although feel free to be creative around it. But remain clean and professional

```html
<!DOCTYPE html>
<html lang="en">
<head>
<meta charset="utf-8">
<title>Harrowgate Building and Property Services – Business Card</title>
<link rel="stylesheet" href="https://fonts.googleapis.com/css2?family=Cinzel:wght@400;600&family=Crimson+Text:wght@400;600&display=swap">
<style>
  :root {
    --canvas-bg: #e9e6e1;
    --card-black: #0b0d10;
    --card-black-soft: #1c2026;
    --brand-blue: #2b9ee3;
    --brand-blue-light: #4fb6ef;
    --brand-blue-deep: #1577c2;
    --ink-navy: #0b2740;
    --text-light: #e7edf3;
  }
  * { margin: 0; padding: 0; box-sizing: border-box; }
  html, body { width: 1200px; height: 843px; overflow: hidden; }
  body {
    background: var(--canvas-bg);
    position: relative;
    font-family: "Crimson Text", Georgia, serif;
  }
  .card {
    position: absolute;
    width: 620px;
    height: 379px;
    border-radius: 6px;
    overflow: hidden;
    box-shadow: 0 10px 28px rgba(0,0,0,0.28);
  }
  .card-back {
    left: 60px; top: 50px;
    background: linear-gradient(160deg, var(--card-black-soft) 0%, var(--card-black) 55%, #050608 100%);
    display: flex; flex-direction: column; align-items: center; justify-content: center;
  }
  .brand-lockup { display: flex; align-items: center; gap: 16px; }
  .brand-square {
    width: 30px; height: 30px;
    background: var(--brand-blue);
  }
  .brand-name {
    font-family: "Cinzel", Georgia, serif;
    font-weight: 400;
    color: var(--brand-blue);
    letter-spacing: 0.08em;
  }
  .card-back .brand-name { font-size: 48px; }
  .brand-tagline {
    font-family: "Cinzel", Georgia, serif;
    color: var(--brand-blue);
    letter-spacing: 0.12em;
    text-transform: uppercase;
  }
  .card-back .brand-tagline { font-size: 14px; margin-top: 10px; }

  .card-front {
    left: 520px; top: 444px;
    background: linear-gradient(165deg, var(--card-black-soft) 0%, var(--card-black) 60%);
  }
  .front-band { position: absolute; inset: 0; }
  .front-header { position: absolute; left: 40px; top: 26px; }
  .front-header .brand-name { font-size: 42px; line-height: 1; }
  .front-header .brand-tagline { font-size: 11.5px; margin-top: 4px; }
  .person-name {
    font-family: "Cinzel", Georgia, serif;
    color: var(--brand-blue);
    font-size: 22px;
    margin-top: 22px;
    letter-spacing: 0.03em;
  }
  .person-role {
    font-family: "Cinzel", Georgia, serif;
    color: var(--text-light);
    font-size: 14px;
    letter-spacing: 0.05em;
  }
  .contact {
    position: absolute; left: 40px; top: 238px;
    color: var(--ink-navy);
    font-size: 16px;
    line-height: 1.35;
  }
  .contact strong { font-weight: 600; }
</style>
</head>
<body>

<section class="card card-back" aria-label="Card back">
  <div class="brand-lockup">
    <span class="brand-square" aria-hidden="true"></span>
    <span class="brand-name">HARROWGATE</span>
  </div>
  <p class="brand-tagline">Building and Property Services</p>
</section>

<section class="card card-front" aria-label="Card front">
  <svg class="front-band" width="620" height="379" viewBox="0 0 620 379" aria-hidden="true">
    <defs>
      <linearGradient id="bandBlue" x1="0" y1="0" x2="1" y2="1">
        <stop offset="0" stop-color="#4fb6ef"/>
        <stop offset="0.55" stop-color="#2b9ee3"/>
        <stop offset="1" stop-color="#1577c2"/>
      </linearGradient>
    </defs>
    <polygon points="0,198 620,232 620,379 0,379" fill="url(#bandBlue)"/>
    <polygon points="0,198 620,232 620,236 0,202" fill="#7fcaf4" opacity="0.6"/>
  </svg>

  <header class="front-header">
    <div class="brand-name">HARROWGATE</div>
    <p class="brand-tagline">Building and Property Services</p>
    <p class="person-name">Duncan Hensley</p>
    <p class="person-role">DIRECTOR</p>
  </header>

  <address class="contact" style="font-style: normal;">
    <div><strong>Phone:</strong> 9218 5371</div>
    <div>dunharrowgate@mailbox-example.net</div>
    <div>Level 17, 88 Marsh Lane</div>
    <div>ELMSWORTH, Melbourne, Vic 3942</div>
  </address>
</section>

</body>
</html>
```